Brookvale Auto Hire- car rental & accident claim management

We need a web design for a company based in Sydney called "Brookvale Auto Hire". We are a rental car company, who also specialise in not at fault accident claim management. when a client is not at fault in an accident, if they can provided us with the At Fault Parties (AFP) insurance details and claim number we can provide them with a rental car whilst their car is repaired (or if it is a total loss) and claim the costs of the rental car from the AFP's insurance company.
-rental vehicles
-accident repalcement vehicles
-third party recovery
-independent assessments
Our fleet comprises of small to large vehicles, including SUV's 4WD's, Prestige and commercial.
Our companies colour is bright green, so we would like it to be in keeping with that. we have two logo's. we would prefer the web page to use a bright/lime green (brighther than our logo).
we would ask that our design communicates quality, commitment to customer service and make our clients feel safe.
our competitors include: Meridian Recoveries and TKL if you would like to peruse these companies to get an idea of our industry. (tkl.example.au and meridianrecoveries.example.au)
Requirements
Must have
- telephone number to come. we are in the middle of chaniging so please leave space for the new phone number (once allocated to us) thank you

```html
<!DOCTYPE html>
<html lang="en">
<head>
<meta charset="utf-8">
<title>Brookvale Auto Hire – Car Rental &amp; Accident Replacement</title>
<link rel="stylesheet" href="https://fonts.googleapis.com/css2?family=Source+Sans+3:wght@400;600;700&display=swap">
<style>
  :root {
    --lime: #8fd15a;
    --lime-light: #c4ec9c;
    --lime-dark: #5fae2d;
    --brand-green: #6cc13f;
    --red: #d8141c;
    --tab-red: #b3161c;
    --ink: #222;
    --grey: #8a8a8a;
    --panel-dark: #1e1e1e;
    --menu-dark: #3a3a3a;
    --line: #b9b9b9;
    --white: #fff;
  }
  * { box-sizing: border-box; margin: 0; padding: 0; }
  html, body { width: 1076px; height: 1200px; overflow: hidden; background: var(--white); }
  body { position: relative; font-family: "Source Sans 3", Arial, sans-serif; color: var(--ink); }
  .abs { position: absolute; }

  .top-strip { left: 0; top: 0; width: 1076px; height: 12px; background: var(--lime); }

  .brand { left: 77px; top: 38px; font-size: 30px; font-weight: 700; color: var(--brand-green); line-height: 1.05; width: 200px; }

  .header-photo { left: 566px; top: 0; width: 107px; height: 117px; background: linear-gradient(180deg, #e7cbb4, #6c4a3a); }

  .call-label { left: 689px; top: 18px; font-size: 34px; font-weight: 700; color: var(--lime); }
  .call-number { left: 686px; top: 48px; font-size: 56px; font-weight: 700; color: var(--red); letter-spacing: -1px; }

  .site-frame { left: 58px; top: 117px; width: 960px; height: 940px; border: 1px solid var(--line); border-radius: 0 0 14px 14px; box-shadow: 0 8px 28px rgba(0,0,0,.18); background: var(--white); }

  .main-nav { left: 58px; top: 117px; width: 708px; height: 28px; background: linear-gradient(180deg, var(--lime-light), var(--lime)); border-radius: 6px 0 0 0; z-index: 4; }
  .main-nav a { position: absolute; top: 0; line-height: 28px; font-size: 19px; color: #111; text-decoration: none; }
  .main-nav a.active { background: var(--panel-dark); color: var(--white); padding: 0 20px; height: 31px; }
  .dropdown { left: 254px; top: 148px; width: 219px; height: 52px; background: var(--menu-dark); border: 1px solid #888; padding: 2px 8px; z-index: 5; }
  .dropdown span { display: block; font-size: 14px; color: var(--white); line-height: 23px; white-space: nowrap; }

  .hero-photo { left: 77px; top: 154px; width: 679px; height: 412px; background: linear-gradient(135deg, #c9ccd0 0%, #e9e4df 45%, #7fa9a0 75%, #5d6066 100%); z-index: 1; }

  .login { left: 769px; top: 123px; width: 235px; height: 128px; background: var(--panel-dark); }
  .login h3 { font-size: 20px; font-weight: 400; color: var(--white); text-align: center; margin-top: 5px; }
  .login .field { width: 214px; height: 20px; margin: 6px auto 0; background: var(--white); border-radius: 10px; font-size: 13px; color: var(--grey); padding-left: 10px; line-height: 20px; }
  .login .register { text-align: center; font-size: 14px; color: #aaa; margin-top: 8px; }

  .quick-head { left: 769px; top: 269px; width: 233px; height: 28px; background: linear-gradient(180deg, var(--lime-light), var(--lime)); border: 1px solid var(--lime-dark); font-size: 18px; font-weight: 600; padding-left: 8px; line-height: 26px; }
  .select { left: 769px; width: 233px; height: 23px; border: 2px solid #555; border-radius: 12px; background: var(--white); font-size: 16px; color: #aaa; padding-left: 8px; line-height: 19px; }
  .select svg { position: absolute; right: -2px; top: -2px; }
  .search-btn { left: 825px; top: 536px; width: 120px; height: 30px; background: linear-gradient(180deg, var(--lime-light), var(--lime)); font-size: 18px; text-align: center; line-height: 30px; }

  .tab-band { left: 59px; top: 581px; width: 958px; height: 68px; background: linear-gradient(180deg, #fff, #d8d8d8); }
  .tab { top: 581px; height: 68px; font-size: 37px; font-weight: 600; color: var(--tab-red); text-align: center; line-height: 60px; }
  .tab-rent { left: 169px; width: 364px; background: var(--white); border: 1px solid var(--line); border-bottom: none; }
  .tab-accident { left: 544px; top: 584px; width: 366px; height: 62px; background: linear-gradient(180deg, #eaeaea, #9c9c9c); line-height: 56px; }

  .fleet-box { left: 59px; top: 649px; width: 958px; height: 190px; border: 1px solid var(--line); border-radius: 0 0 10px 10px; background: var(--white); }
  .fleet-photo { top: 665px; height: 127px; box-shadow: 0 2px 6px rgba(0,0,0,.25); }
  .fleet-label { top: 796px; font-size: 27px; color: var(--lime); }

  .section-title { top: 865px; font-size: 27px; color: var(--lime); }
  .copy { top: 904px; width: 430px; font-size: 18px; line-height: 20px; }
  .copy p { position: relative; padding-left: 34px; margin-bottom: 20px; }
  .copy p::before { content: ""; position: absolute; left: 6px; top: 5px; width: 10px; height: 10px; border-radius: 50%; background: var(--red); }

  .footer { left: 0; top: 1073px; width: 1076px; height: 127px; background: var(--lime); }
  .footer-links { left: 0; top: 1083px; width: 1076px; text-align: center; font-size: 13px; font-weight: 600; color: #111; }
  .copyright { left: 80px; top: 1164px; font-size: 10px; color: #111; }
  .social { top: 1122px; height: 57px; display: flex; align-items: center; gap: 6px; font-size: 16px; font-weight: 600; color: var(--white); }
  .social i { display: block; width: 14px; height: 14px; background: var(--white); }
</style>
</head>
<body>
  <div class="abs top-strip"></div>

  <div class="abs brand">Brookvale<br>Auto Hire</div>
  <div class="abs header-photo" role="img" aria-label="Smiling woman talking on a phone"></div>
  <div class="abs call-label">CALL US:</div>
  <div class="abs call-number">0800 555 010</div>

  <div class="abs site-frame"></div>

  <nav class="abs main-nav">
    <a style="left:26px">Home</a>
    <a style="left:114px">Rentals</a>
    <a class="active" style="left:196px">Accident repalcement</a>
    <a style="left:442px">Services</a>
    <a style="left:546px">Contact Us</a>
  </nav>

  <div class="abs hero-photo" role="img" aria-label="Smiling woman in a silver car holding up the keys"></div>

  <div class="abs dropdown">
    <span>Non Fault Replacment Vehicle</span>
    <span>In Fault Replacment Vehicle</span>
  </div>

  <form class="abs login">
    <h3>Login</h3>
    <div class="field">Username</div>
    <div class="field">Password</div>
    <div class="register">Register</div>
  </form>

  <div class="abs quick-head">Quick Search</div>
  <div class="abs select" style="top:329px">location<svg width="25" height="23" viewBox="0 0 25 23"><circle cx="12.5" cy="11.5" r="10.5" fill="var(--red)" stroke="var(--lime-dark)" stroke-width="2"/><path d="M8 9l4.5 5 4.5-5z" fill="#111"/></svg></div>
  <div class="abs select" style="top:366px">car type<svg width="25" height="23" viewBox="0 0 25 23"><circle cx="12.5" cy="11.5" r="10.5" fill="var(--red)" stroke="var(--lime-dark)" stroke-width="2"/><path d="M8 9l4.5 5 4.5-5z" fill="#111"/></svg></div>
  <div class="abs select" style="top:404px">rent<svg width="25" height="23" viewBox="0 0 25 23"><circle cx="12.5" cy="11.5" r="10.5" fill="var(--red)" stroke="var(--lime-dark)" stroke-width="2"/><path d="M8 9l4.5 5 4.5-5z" fill="#111"/></svg></div>
  <div class="abs select" style="top:444px;color:#444">……………<svg width="25" height="23" viewBox="0 0 25 23"><circle cx="12.5" cy="11.5" r="10.5" fill="var(--red)" stroke="var(--lime-dark)" stroke-width="2"/><path d="M8 9l4.5 5 4.5-5z" fill="#111"/></svg></div>
  <div class="abs select" style="top:486px;color:#444">……………<svg width="25" height="23" viewBox="0 0 25 23"><circle cx="12.5" cy="11.5" r="10.5" fill="var(--red)" stroke="var(--lime-dark)" stroke-width="2"/><path d="M8 9l4.5 5 4.5-5z" fill="#111"/></svg></div>
  <div class="abs search-btn">Search</div>

  <div class="abs tab-band"></div>
  <div class="abs tab tab-accident">Accident replacment</div>
  <div class="abs tab tab-rent">Rent a car</div>

  <div class="abs fleet-box"></div>
  <div class="abs fleet-photo" style="left:77px;width:197px;background:linear-gradient(180deg,#f2f2f4,#c9c9d0)" role="img" aria-label="Small white city car"></div>
  <div class="abs fleet-photo" style="left:283px;width:164px;background:linear-gradient(180deg,#fafafa,#b7b9bc)" role="img" aria-label="Silver mid-size sedan"></div>
  <div class="abs fleet-photo" style="left:456px;width:196px;background:linear-gradient(180deg,#a9a49c,#2d3346)" role="img" aria-label="Dark blue SUV parked outside a house"></div>
  <div class="abs fleet-photo" style="left:661px;width:164px;background:linear-gradient(160deg,#7a7d82,#8d2a22 60%,#4b3b2e)" role="img" aria-label="Red four-wheel drive climbing rocks"></div>
  <div class="abs fleet-photo" style="left:835px;width:167px;background:linear-gradient(180deg,#f0f0f0,#c9b08c)" role="img" aria-label="White commercial van loaded with boxes"></div>
  <div class="abs fleet-label" style="left:74px">mini</div>
  <div class="abs fleet-label" style="left:283px">midle</div>
  <div class="abs fleet-label" style="left:459px">SUV's</div>
  <div class="abs fleet-label" style="left:661px">4WD</div>
  <div class="abs fleet-label" style="left:836px">comercial</div>

  <h2 class="abs section-title" style="left:78px;font-weight:400">About Brookvale Auto Hire</h2>
  <div class="abs copy" style="left:104px">
    <p>The newcastle depot manager was very profes-<br>sional, and wanted to ensure my happiness at every opportunity, so was his offsider/co-worker.<br>I wish your company all the best.</p>
    <p>The newcastle depot manager was very profes-<br>sional, and wanted to ensure my happiness at</p>
  </div>

  <h2 class="abs section-title" style="left:553px;font-weight:400">Customer Feedback</h2>
  <div class="abs copy" style="left:573px">
    <p>The newcastle depot manager was very profes-<br>sional, and wanted to ensure my happiness at every opportunity, so was his offsider/co-worker.<br>I wish your company all the best.</p>
    <p>The newcastle depot manager was very profes-<br>sional, and wanted to ensure my happiness at every</p>
  </div>

  <footer class="abs footer"></footer>
  <div class="abs footer-links">Home / Claim Form / Partners / Why Brookvale Auto Hire / Services / F AQs / Contact Us / Site Map / Privacy Policy / Disclaimer</div>
  <div class="abs copyright">Brookvale Auto Hire, All Rights Reserved, Copyright © 2012</div>
  <div class="abs social" style="left:860px"><i></i>Linkwave</div>
  <div class="abs social" style="left:958px"><i></i>Chirpline</div>
</body>
</html>
```